依頼詳細
販売する水産物ですが、安売りではなく単価の高い水産物なので美味しさだけでなく高級感も感じさせるデザインで白を基調としたイメージでお願いします。
記載項目
浜栄水産/0983-47-1852/http://www.kaisuzuka.co.jp//潮風の便り/ロゴ(webサイトのロゴを使ってください。)
サイズ
基本はB2ですがお任せします。
ページ数
片面
希望イメージ
シンプル 複雑
単色 カラフル
暗い 明るい
日常 高級
遊び心 厳粛
未来的 伝統的
女性的 男性的
希望する色
白を基調とした高級感が伝わるような感じでお願いします。
納品ファイル
• 高解像度JPG (.jpg)
• イラストレーター形式 (.ai)
補足説明
参考URL/http://www.kaisuzuka.co.jp/
当社の水産物は大都市圏で高い評価をいただいている水産物です。
その理由として他社に負けない取扱いで出荷しています。
その思いをポスターに伝える表現でお願いします。

ポスターで使う水産物の写真は
http://www.kaisuzuka.co.jp/blog/
から利用してください。

天然の真鯛の写真はは当社の看板商品なので必ず使用してください。
・真鯛の写真が少なかったのでブログに追加しました。

・ロゴですが綺麗に収まるのであれば利用しなくても大丈夫です。
高級感が伝わり産地がわかるポスターであればお任せします。
■ 選んだ理由

今回、どの案も素晴らしく決定にかなり悩みました。
その中でシンプルで伝えたいことが分かりやすく、ブランド名がはっきり分かりやすい案を、数種類選びだし関係する方からの意見も聞き総合評価で決定しました。

■ 提案者全員のお礼・コメント

今回、提案していただい方々ありがとうございました。
どの案も素晴らしく予算があればもっとと思うことが多々あり大変でした。

今回、審査途中でコメントを入れようか悩みましたが提案の意味や提案者の素の能力をできるだけ見極めたいのでしませんでした。

このような時間をかけた提案をした方々に、何も返答しない非礼をここでお詫びさせてください。

また、他の案件も考えているので、出来ればまたよろしくお願い致します。
ありがとうございました。

```html
<!DOCTYPE html>
<html lang="ja">
<head>
<meta charset="utf-8">
<title>潮風の便り｜浜栄水産</title>
<link rel="stylesheet" href="https://fonts.googleapis.com/css2?family=Zen+Old+Mincho:wght@400;700;900&family=Noto+Serif+JP:wght@400;600;700&family=Noto+Sans+JP:wght@400;700&display=swap">
<style>
  :root{
    --navy:#1b2a4a;
    --navy-deep:#111c33;
    --seal:#b3262b;
    --ink:#1c1c1c;
    --body:#3a3a3a;
    --paper:#ffffff;
    --rule:#d8d8d8;
    --fish-light:#f4e6e2;
    --fish-red:#d8776a;
    --footer:#f1f1f1;
  }
  *{margin:0;padding:0;box-sizing:border-box}
  html,body{width:848px;height:1200px;overflow:hidden;background:var(--paper)}
  .poster{position:relative;width:848px;height:1200px;background:var(--paper);font-family:"Noto Serif JP",serif;color:var(--ink)}
  .hero-photo{position:absolute;left:0;top:0;width:848px;height:600px;
    background:
      radial-gradient(ellipse 40% 30% at 12% 8%, rgba(70,110,70,.55), transparent 70%),
      radial-gradient(ellipse 30% 25% at 92% 70%, rgba(70,110,70,.45), transparent 70%),
      linear-gradient(160deg,#f6eeea 0%,#e9a898 35%,#d9786a 55%,#f1d9d2 80%,#ffffff 100%);}
  .hero-fade{position:absolute;left:0;top:440px;width:848px;height:170px;background:linear-gradient(to bottom,rgba(255,255,255,0),#fff 85%)}
  .brand-disc{position:absolute;right:-40px;top:-70px;width:420px;height:420px;border-radius:50%;background:radial-gradient(circle at 40% 40%,var(--navy),var(--navy-deep));}
  .brand-origin{position:absolute;left:582px;top:22px;color:#fff;font-family:"Zen Old Mincho",serif;font-size:15px;letter-spacing:.08em;font-weight:700}
  .brand-origin small{font-size:11px;margin-left:8px;font-weight:400}
  .brand-name{position:absolute;left:520px;top:60px;width:300px;color:#fff;font-family:"Zen Old Mincho",serif;font-weight:900;font-size:76px;line-height:1.08;letter-spacing:.02em}
  .brand-name .line2{display:block;padding-left:90px}
  .brand-seal{position:absolute;left:790px;top:210px;width:28px;height:44px;background:var(--seal);border-radius:3px}
  .headline{position:absolute;left:50px;top:572px;font-family:"Zen Old Mincho",serif;font-weight:900;font-size:38px;line-height:1.5;letter-spacing:.04em;color:var(--ink)}
  .sub-head{position:absolute;left:50px;top:680px;font-weight:700;font-size:16px;line-height:1.55;color:var(--navy)}
  .intro{position:absolute;left:50px;top:730px;width:400px;font-size:10.5px;line-height:1.75;color:var(--body)}
  .catalog{position:absolute;left:22px;top:820px;width:804px;display:grid;grid-template-columns:repeat(4,1fr);gap:6px}
  .item{position:relative;height:150px}
  .item-photo{width:100%;height:100%}
  .item-label{position:absolute;left:8px;top:6px;font-family:"Zen Old Mincho",serif;font-weight:700;font-size:12px;color:#fff;text-shadow:0 0 0 transparent}
  .footer{position:absolute;left:0;top:1150px;width:848px;height:50px;background:var(--footer);display:flex;align-items:center;padding:0 38px;border-top:1px solid var(--rule)}
  .footer-name{font-family:"Zen Old Mincho",serif;font-weight:900;font-size:22px;letter-spacing:.06em;color:var(--ink);display:flex;align-items:center;gap:8px}
  .footer-name::before{content:"";width:14px;height:14px;background:var(--navy);display:inline-block}
  .footer-tel{margin-left:18px;font-family:"Noto Sans JP",sans-serif;font-size:18px;font-weight:700}
  .footer-tel small{font-size:11px;font-weight:400;margin-right:3px}
  .footer-url{margin-left:auto;font-family:"Noto Serif JP",serif;font-size:18px;font-weight:600;letter-spacing:.02em}
</style>
</head>
<body>
<main class="poster">
  <div class="hero-photo" role="img" aria-label="氷の上に並んだ天然真鯛と緑の海藻の写真"></div>
  <div class="hero-fade"></div>

  <div class="brand-disc"></div>
  <p class="brand-origin">豊後水道<small>大分県佐伯市</small></p>
  <h1 class="brand-name">潮風の<span class="line2">便り</span></h1>
  <div class="brand-seal"></div>

  <p class="headline">黒潮と瀬戸内海の<br>潮の恵みをめしあがれ。</p>

  <p class="sub-head">豊後水道で水揚げした<br>浜栄水産最高品質の水産物</p>
  <p class="intro">豊後水道と瀬戸内海の潮がぶつかる日本有数の魚場<br>豊後水道の恵みを受け、<br>創業から培ってきた確かな「信用」で大都市圏の<br>様々な業者様に「日本一の魚」と高い評価をいただいております。</p>

  <section class="catalog">
    <div class="item"><div class="item-photo" role="img" aria-label="真鯛の写真" style="background:linear-gradient(135deg,#d77a6c,#f3d8d0)"></div><span class="item-label">真鯛</span></div>
    <div class="item"><div class="item-photo" role="img" aria-label="並んだ鯖の写真" style="background:linear-gradient(135deg,#4d6a6a,#b9c8c4)"></div><span class="item-label">鯖類</span></div>
    <div class="item"><div class="item-photo" role="img" aria-label="黒い魚の写真" style="background:linear-gradient(135deg,#3a3f48,#9aa0a8)"></div><span class="item-label">黒鯛</span></div>
    <div class="item"><div class="item-photo" role="img" aria-label="大型の青魚の写真" style="background:linear-gradient(135deg,#5d7790,#e3e8ee)"></div><span class="item-label">平政</span></div>
    <div class="item"><div class="item-photo" role="img" aria-label="蟹の写真" style="background:linear-gradient(135deg,#a9432e,#e7a07f)"></div><span class="item-label">渡蟹</span></div>
    <div class="item"><div class="item-photo" role="img" aria-label="並んだ鯵の写真" style="background:linear-gradient(135deg,#6d7b88,#d6dde3)"></div><span class="item-label">真鯵</span></div>
    <div class="item"><div class="item-photo" role="img" aria-label="巻貝の写真" style="background:linear-gradient(135deg,#8a6e52,#e2d3bf)"></div><span class="item-label">夜光貝</span></div>
    <div class="item"><div class="item-photo" role="img" aria-label="二枚貝の写真" style="background:linear-gradient(135deg,#9c8f80,#efe9e1)"></div><span class="item-label">蛤</span></div>
  </section>

  <footer class="footer">
    <span class="footer-name">浜栄水産</span>
    <span class="footer-tel"><small>tel.</small>0983-47-1852</span>
    <span class="footer-url">http://www.kaisuzuka.co.jp/</span>
  </footer>
</main>
</body>
</html>
```